Fairway Circuit web site

Fairway Circuit is a High End golf amateur Tour targeted to wealthy golf passionates.
The concept is to take average golfers and offer them the same playing conditions than the pros (Caddies, branded bags, TV coverage...) and bring them to the most beautiful golf courses around the world.
Keywords: International, Exclusive, Luxury, but not show-off...
The Task is to design the WordPress template and a exemple page.
Please use the provided logo and any stock image you like.
Updates

Hello,

please note that the outcome has to be a fully coded WordPress site.

Please no "Photoshop only" designs...

Thanks

```html
<!DOCTYPE html>
<html lang="en">
<head>
<meta charset="utf-8">
<title>Fairway Circuit</title>
<link href="https://fonts.googleapis.com/css2?family=Open+Sans:wght@400;600;700&display=swap" rel="stylesheet">
<style>
:root{
  --green:#0f4b2f;
  --green-text:#1b5a3a;
  --gold:#bf8a3c;
  --gold-dark:#a8772f;
  --text:#6a6a6a;
  --cream:#f7f4ea;
  --footer:#3a3a3a;
  --white:#ffffff;
}
*{box-sizing:border-box;margin:0;padding:0}
html,body{width:780px;height:1200px;overflow:hidden}
body{font-family:"Open Sans",sans-serif;position:relative;color:var(--text);
  background:linear-gradient(180deg,#8fc0e8 0,#b9d3a0 40px,#7fae55 120px,#9fc276 300px,#e9ecd4 370px,var(--cream) 420px,#fbfaf5 100%)}
.abs{position:absolute}
a{text-decoration:none;color:inherit}

/* header */
.utility{top:14px;left:528px;font-size:7px;font-weight:600;color:#333;letter-spacing:.2px}
.utility .reg{color:var(--gold)}
.search{top:10px;left:634px;width:97px;height:18px;background:var(--white)}
.search svg{position:absolute;right:4px;top:4px}
.navbar{top:38px;left:0;width:780px;height:36px;background:linear-gradient(#fafafa,#ececec)}
.nav{top:52px;left:185px;display:flex;gap:0;font-size:8px;font-weight:600;color:var(--green-text)}
.nav span{margin-right:22px}
.nav span:last-child{margin-right:0}
.logo{top:8px;left:56px;width:92px;height:92px;border-radius:50%;background:var(--white);
  border:3px solid var(--gold);display:flex;align-items:center;justify-content:center;text-align:center;
  font-size:11px;font-weight:700;color:var(--green);line-height:1.2;box-shadow:0 2px 4px rgba(0,0,0,.2)}

/* hero */
.hero{top:80px;left:48px;width:684px;height:268px;border:3px solid var(--white);box-shadow:0 1px 3px rgba(0,0,0,.3)}
.hero-img{width:100%;height:100%;background:linear-gradient(90deg,#6b6a4e,#8a7b66 30%,#5d79b8 55%,#7d6a5a 80%,#4e5a3c)}
.hero-cap{position:absolute;left:0;bottom:0;width:100%;height:60px;background:rgba(20,20,20,.72);
  color:var(--white);font-size:18px;font-weight:600;line-height:18px;padding:10px 12px}
.arrow{position:absolute;top:119px;width:22px;height:24px;background:rgba(0,0,0,.55)}
.arrow.l{left:0}.arrow.r{right:0}

/* scoreboard */
.h-sec{font-size:12px;font-weight:600;color:#222;letter-spacing:.3px}
.scoreboard{top:390px;left:48px;width:450px;height:183px;background:var(--green);border:2px solid var(--gold)}
.sb-head{display:flex;font-size:7px;color:var(--white);padding:10px 0 0 12px;height:24px;border-bottom:1px solid #2e6a4c}
.sb-row{display:flex;font-size:7px;color:var(--white);margin:0 10px 0 12px;height:22.3px;align-items:center;border-bottom:1px solid #2e6a4c}
.c1{width:44px}.c2{width:87px}.c3{width:109px}.c4{width:51px}.c5{width:55px}
.sb-row .c1{width:44px}
.sb-btn{position:absolute;left:9px;bottom:6px;width:428px;height:24px;background:var(--gold);color:var(--white);
  font-size:9px;font-weight:600;display:flex;align-items:center;justify-content:center}

.tabs{top:370px;left:516px;display:flex;font-size:9px;font-weight:600}
.tab{height:24px;display:flex;align-items:center;padding:0 18px}
.tab.on{background:var(--gold);color:var(--white)}
.tab.off{color:var(--green-text);padding:0 10px}
.news-box{top:394px;left:516px;width:216px;height:180px;border:3px solid var(--gold);background:var(--white);padding:9px 8px 0 18px}
.news-box li{font-size:7.5px;color:var(--green-text);line-height:12px;margin-bottom:6px;list-style:none;position:relative}
.news-box li::before{content:"";position:absolute;left:-10px;top:4px;width:4px;height:4px;border-radius:50%;background:var(--gold)}

/* tournaments */
.tourn{top:588px;left:48px;width:683px;height:172px;border:1px solid var(--gold);background:var(--white)}
.tourn-head{height:30px;background:var(--green);color:var(--white);font-size:12px;font-weight:600;padding:7px 10px;position:relative}
.tourn-head svg{position:absolute;right:8px;top:9px}
.t-img{position:absolute;top:43px;width:145px;height:110px;border:2px solid #e6e6e6}
.t-txt{position:absolute;top:45px;width:160px}
.t-title{font-size:9px;font-weight:600;color:var(--gold);line-height:12px;margin-bottom:3px}
.t-body{font-size:7.5px;line-height:13.7px}
.t-more{font-size:7.5px;font-weight:600;color:var(--green-text);margin-top:5px}

/* photos */
.ptabs{top:777px;left:48px;display:flex;font-size:8px;font-weight:600}
.ptabs .tab{height:25px;padding:0 9px}
.ptabs .tab.off{padding:0 7px}
.photos{top:802px;left:48px;width:509px;height:179px;border:3px solid var(--gold);background:var(--white)}
.ph{position:absolute}
.ph-cap{position:absolute;left:10px;top:157px;font-size:8.5px;color:var(--green-text)}
.ph-btn{position:absolute;left:438px;top:149px;width:56px;height:20px;background:var(--green);color:var(--white);font-size:7.5px;font-weight:600;display:flex;align-items:center;justify-content:center}

.latest{top:777px;left:574px;width:157px;height:204px;background:var(--green);border:2px solid var(--gold)}
.latest-head{height:24px;background:var(--gold);color:var(--white);font-size:11.5px;font-weight:600;padding:3px 8px}
.ln{padding:11px 10px 0;font-size:7.5px;line-height:11.5px;color:var(--white)}
.ln b{display:block;color:var(--gold);font-weight:400}
.ln + .ln{padding-top:8px}
.ln-btn{position:absolute;left:10px;bottom:10px;width:78px;height:22px;background:var(--gold);color:var(--white);font-size:7.5px;font-weight:600;display:flex;align-items:center;justify-content:center}

/* partners */
.partners-title{top:995px;left:0;width:780px;text-align:center}
.partner{top:1018px;width:215px;height:72px;border:1.5px solid var(--gold-dark);background:var(--white)}
.p-mark{position:absolute;left:9px;top:24px;width:70px;display:flex;align-items:center;gap:4px;font-size:10px;font-weight:700;color:var(--green)}
.p-mark i{display:inline-block;width:10px;height:10px;border-radius:50%;background:var(--green)}
.p-txt{position:absolute;left:77px;top:11px;width:132px}
.p-name{font-size:8.5px;font-weight:600;color:var(--green-text);margin-bottom:2px}
.p-body{font-size:7.5px;line-height:12px}

/* footer */
.footer{top:1102px;left:0;width:780px;height:98px;background:var(--footer)}
.f-links{position:absolute;left:48px;top:20px;font-size:7px;color:var(--gold)}
.f-links span{color:#888;margin:0 3px}
.f-logo{position:absolute;left:48px;top:42px;width:48px;height:48px;border-radius:50%;background:var(--white);
  display:flex;align-items:center;justify-content:center;text-align:center;font-size:6px;font-weight:700;color:var(--green);line-height:1.15}
.f-copy{position:absolute;left:110px;top:60px;font-size:7px;color:#ccc}
.f-h{position:absolute;font-size:9.5px;color:var(--white)}
.f-email{position:absolute;left:296px;top:38px;width:148px;height:20px;background:#f0f0f0;font-size:7.5px;color:#999;padding:5px 9px}
.f-sign{position:absolute;left:449px;top:38px;width:48px;height:20px;background:var(--gold);color:var(--white);font-size:7.5px;font-weight:600;display:flex;align-items:center;justify-content:center}
.social{position:absolute;left:625px;top:40px;display:flex;gap:4px}
.social i{width:18px;height:18px;border-radius:50%;background:var(--white);border:2px solid #666}
</style>
</head>
<body>

<div class="abs navbar"></div>
<div class="abs utility">MEMBER LOGIN &nbsp;| &nbsp;<span class="reg">REGISTER</span></div>
<div class="abs search"><svg width="10" height="10" viewBox="0 0 10 10"><circle cx="6" cy="4" r="3" fill="none" stroke="#bf8a3c" stroke-width="1.5"/><line x1="4" y1="6" x2="1" y2="9" stroke="#bf8a3c" stroke-width="2"/></svg></div>
<nav class="abs nav"><span>HOME</span><span>ABOUT US</span><span>TOUR</span><span>PARTNERS</span><span>TOURNAMENTS</span><span>PLAYERS</span><span>STATS</span><span>GALLERY</span><span>NEWS</span><span>CONTACT US</span></nav>

<section class="abs hero">
  <div class="hero-img" role="img" aria-label="Golfer finishing a swing in front of a watching crowd"></div>
  <div class="arrow l"><svg width="22" height="24"><polyline points="13,7 8,12 13,17" fill="none" stroke="#fff" stroke-width="1.2"/></svg></div>
  <div class="arrow r"><svg width="22" height="24"><polyline points="9,7 14,12 9,17" fill="none" stroke="#fff" stroke-width="1.2"/></svg></div>
  <div class="hero-cap">Aliquam ullamcorper tempor felis, nec condimentum odio aliquet vitae.</div>
</section>
<div class="abs logo">Fairway<br>Circuit</div>

<h2 class="abs h-sec" style="top:368px;left:48px">SCORE BOARD</h2>
<section class="abs scoreboard">
  <div class="sb-head"><span class="c1">RANK</span><span class="c2">LAST WEEK RANK</span><span class="c3">PLAYER</span><span class="c4">EVENTS</span><span class="c5">POINTS</span><span>POINTS BEHIND LEAD</span></div>
  <div style="height:8px"></div>
  <div class="sb-row"><span class="c1">1</span><span class="c2">5</span><span class="c3">Lena Marsh</span><span class="c4">4</span><span class="c5">921</span><span></span></div>
  <div class="sb-row"><span class="c1">2</span><span class="c2">2</span><span class="c3">Tessa Hale</span><span class="c4">3</span><span class="c5">742</span><span>179</span></div>
  <div class="sb-row"><span class="c1">3</span><span class="c2">1</span><span class="c3">Mira Cole</span><span class="c4">4</span><span class="c5">587</span><span>334</span></div>
  <div class="sb-row"><span class="c1">4</span><span class="c2">3</span><span class="c3">Ella Varga</span><span class="c4">3</span><span class="c5">573</span><span>348</span></div>
  <div class="sb-row" style="border:none"><span class="c1">5</span><span class="c2">4</span><span class="c3">Nora Pike</span><span class="c4">4</span><span class="c5">541</span><span>380</span></div>
  <div class="sb-btn">More About Score</div>
</section>

<div class="abs tabs"><div class="tab on">RECENT NEWS</div><div class="tab off">MOST POPULAR</div></div>
<ul class="abs news-box">
  <li>Aliquam molestie, mi et imperdiet euismod, dui purus auctor tellus..</li>
  <li>Aliquam molestie, mi et imperdiet euismod.</li>
  <li>Suspendisse lobortis turpis in odio blandit ac interdum lorem euismod. Etiam risus massa.</li>
  <li>Aliquam molestie, mi et imperdiet euismod, dui purus auctor tellus..</li>
  <li>Aliquam molestie, mi et imperdiet euismod.</li>
  <li>Suspendisse lobortis turpis in odio blandit ac interdum lorem euismod.</li>
</ul>

<section class="abs tourn">
  <div class="tourn-head">FEATURED TOURNAMENTS<svg width="18" height="12"><polyline points="2,1 7,6 2,11" fill="none" stroke="#fff" stroke-width="1.3"/><polyline points="10,1 15,6 10,11" fill="none" stroke="#fff" stroke-width="1.3"/></svg></div>
  <div class="t-img" style="left:12px;background:linear-gradient(135deg,#6b9ed6,#c9a97a 50%,#3a9a4a)" role="img" aria-label="Golfer holding a trophy and a club"></div>
  <div class="t-txt" style="left:166px">
    <div class="t-title">Lorem ipsum dolor sit amet, consectetur adipiscing elit.</div>
    <div class="t-body">In congue, neque ac lobortis volutpat, libero mauris varius mi, vitae suscipit ipsum ligula vitae risus. Duis aliquam nibh a dui iaculis viverra id a velit. Vivamus egestas risus in magna varius commodo.</div>
    <div class="t-more">READ MORE</div>
  </div>
  <div class="t-img" style="left:358px;background:linear-gradient(180deg,#3d5a2e,#5e8a3e 45%,#8cbf5a)" role="img" aria-label="Players walking on a green beside the flag"></div>
  <div class="t-txt" style="left:512px">
    <div class="t-title">Lorem ipsum dolor sit amet, consectetur adipiscing elit.</div>
    <div class="t-body">In congue, neque ac lobortis volutpat, libero mauris varius mi, vitae suscipit ipsum ligula vitae risus. Duis aliquam nibh a dui iaculis viverra id a velit. Vivamus egestas risus in magna varius commodo.</div>
    <div class="t-more">READ MORE</div>
  </div>
</section>

<div class="abs ptabs"><div class="tab on">FEATURED PHOTOS</div><div class="tab off" style="color:var(--green-text)">FEATURED VIDEOS</div></div>
<section class="abs photos">
  <div class="ph" style="left:10px;top:9px;width:221px;height:136px;background:linear-gradient(180deg,#3f5f2c,#7aa84d 50%,#a9cf7a)" role="img" aria-label="Golfer in red walking across the green"></div>
  <div class="ph" style="left:247px;top:9px;width:117px;height:63px;background:linear-gradient(90deg,#2a2a2a,#b85050 30%,#4d8a5a 60%,#cfcfcf)" role="img" aria-label="Group of players posing at an open event"></div>
  <div class="ph" style="left:376px;top:9px;width:118px;height:63px;background:linear-gradient(180deg,#6a7a4a,#c7a56a 50%,#6b9a40)" role="img" aria-label="Player raising a trophy"></div>
  <div class="ph" style="left:247px;top:81px;width:117px;height:64px;background:linear-gradient(135deg,#8a7a66,#c99a7a 50%,#5a4a3a)" role="img" aria-label="Smiling golfer in a cap"></div>
  <div class="ph" style="left:376px;top:81px;width:118px;height:64px;background:linear-gradient(180deg,#a6c27a,#d8c84a 50%,#7aa64a)" role="img" aria-label="Golfer crouching to read the green"></div>
  <div class="ph-cap">Aliquam ullamcorper tempor felis</div>
  <div class="ph-btn">VIEW ALL</div>
</section>

<section class="abs latest">
  <div class="latest-head">LATEST NEWS</div>
  <div class="ln"><b>MAR 15, 2014</b>Aliquam molestie, mi et imperdiet euismod dui purus..</div>
  <div class="ln"><b>MAR 15, 2014</b>Aliquam molestie, mi et imperdiet euismod dui purus..</div>
  <div class="ln"><b>MAR 15, 2014</b>Aliquam molestie, mi et imperdiet euismod dui purus..</div>
  <div class="ln-btn">READ ALL NEWS</div>
</section>

<h2 class="abs h-sec partners-title">FEATURED PARTNERS</h2>
<div class="abs partner" style="left:48px">
  <div class="p-mark"><i></i>Norvik</div>
  <div class="p-txt"><div class="p-name">NORVIK</div><div class="p-body">In congue, neque ac lobortis volutpat, libero mauris varius mi, vitae suscipit ipsum..</div></div>
</div>
<div class="abs partner" style="left:282px">
  <div class="p-mark"><i></i>Coronet</div>
  <div class="p-txt" style="left:82px"><div class="p-name">CORONET</div><div class="p-body">In congue, neque ac lobortis volutpat, libero mauris varius mi, vitae suscipit ipsum..</div></div>
</div>
<div class="abs partner" style="left:517px">
  <div class="p-mark"><i></i>Parline</div>
  <div class="p-txt" style="left:80px"><div class="p-name">PARLINE</div><div class="p-body">In congue, neque ac lobortis volutpat, libero mauris varius mi, vitae suscipit ipsum..</div></div>
</div>

<footer class="abs footer">
  <div class="f-links">Home<span>/</span>About Us<span>/</span>Contact<span>/</span>Jobs<span>/</span>Advertise</div>
  <div class="f-logo">Fairway<br>Circuit</div>
  <div class="f-copy">© 2014. Fairway Circuit All Right Reserved</div>
  <div class="f-h" style="left:296px;top:16px">Sign Up for our E-Newsletter</div>
  <div class="f-email">Enter Email Address</div>
  <div class="f-sign">SIGN UP</div>
  <div class="f-h" style="left:625px;top:16px">Follow Us</div>
  <div class="social"><i></i><i></i><i></i><i></i><i></i></div>
</footer>

</body>
</html>
```